Organic Food company needs a new design label logo

Our company name is Brackenmoor Organic. We pack organic dried products and sell to natural, organic or small supermarkets in the UK.

We would like to you to design our new label with logo.

The label size should be the width is 65 mm and the length is 85 mm. The label should also include our tillbrook council and European organic logos.

The food label should reflect our company that we are organic and we sell quality organic food products.

The colours should be pastel and warm colour. It shouldn’t have so many colour.

Dear All,

Just let you know that this project is food label with the new design. The size of the label should as follow; 
width: 65 mm
length: 85 mm

It will be used for dried fruit, vegetables and nuts. so the middle of the label should be blank, as the print shop will print the name separetly.

When you design our new logo label, please also read my previous note.

Thank you.

Target Market(s)

Above 25 years old. People who like to buy organic or natural food products. Middle income people.

Industry/Entity Type

It Company

Requirements
Must have
• 1) Tillbrook Council logo (attached as file )

2) European organic logo ( can be download from http://ab.quorvanet.org/farming/green/mark-policy/badge_en )

3) The following information should be either next to or underneath to European logo;
GB-TRV-38
Non-EU Agriculture

The above text information shouldn't be very big.

4) There should be enough space in the middle of the label to write (later by the print shop) full product name and weight.

5) Our company name is "Brackenmoor Organic"

6) Our web site address is www.brackenmoor.com

```html
<!DOCTYPE html>
<html lang="en">
<head>
<meta charset="utf-8">
<title>Brackenmoor Organic – Label Variations</title>
<link rel="stylesheet" href="https://fonts.googleapis.com/css2?family=Mulish:wght@400;700&display=swap">
<style>
  :root {
    --stage-centre: #6b7462;
    --stage-edge: #6f6a4c;
    --forest: #013d1e;
    --leaf: #7dc242;
    --stone: #c2b59c;
    --cream: #e1ecc3;
    --badge-green: #8cc63f;
    --frame-line: #b9c2ad;
    --ink: #141414;
  }
  html, body {
    margin: 0;
    padding: 0;
    width: 1200px;
    height: 900px;
    overflow: hidden;
  }
  body {
    position: relative;
    background: radial-gradient(ellipse at center, var(--stage-centre) 55%, var(--stage-edge) 100%);
    font-family: "Mulish", "Century Gothic", sans-serif;
  }
  .label {
    position: absolute;
    top: 118px;
    width: 296px;
    height: 386px;
    box-sizing: border-box;
    border: 10px solid;
  }
  .label--leaf  { left: 74px;  border-color: var(--leaf);  background: var(--forest); --name: var(--leaf);  --mark: var(--leaf); }
  .label--stone { left: 451px; border-color: var(--stone); background: var(--forest); --name: var(--cream); --mark: var(--stone); }
  .label--cream { left: 830px; border-color: var(--forest); background: var(--cream); --name: var(--forest); --mark: var(--forest); }

  .brand-mark {
    position: absolute;
    left: 50%;
    top: 30px;
    width: 84px;
    height: 84px;
    margin-left: -42px;
    border-radius: 50%;
    background: var(--mark);
  }
  .brand-name {
    position: absolute;
    left: 0;
    right: 0;
    top: 130px;
    margin: 0;
    text-align: center;
    font-weight: 700;
    font-size: 30px;
    line-height: 33px;
    letter-spacing: -0.5px;
    color: var(--name);
  }
  .product-frame {
    position: absolute;
    left: 20px;
    top: 199px;
    width: 236px;
    height: 106px;
    box-sizing: border-box;
    border: 1px solid var(--frame-line);
  }
  .label--cream .product-frame { border-color: #8a8f80; }
  .product-space {
    position: absolute;
    left: 11px;
    top: 12px;
    right: 11px;
    bottom: 12px;
    background: var(--cream);
  }
  .label--cream .product-space { display: none; }

  .certification {
    position: absolute;
    left: 69px;
    top: 320px;
    display: flex;
    align-items: center;
    gap: 10px;
  }
  .certification__council {
    width: 28px;
    height: 28px;
    box-sizing: border-box;
    border-radius: 50%;
    border: 2px solid var(--cream);
  }
  .label--cream .certification__council { border-color: var(--forest); }
  .certification__eu {
    width: 41px;
    height: 28px;
    background: var(--badge-green);
  }
  .certification__code {
    margin: 0;
    font-size: 8px;
    line-height: 10px;
    color: var(--cream);
  }
  .label--cream .certification__code { color: var(--forest); }

  .master-logo {
    position: absolute;
    left: 0;
    right: 0;
    top: 590px;
    text-align: center;
  }
  .master-logo .brand-mark {
    position: relative;
    display: block;
    top: 0;
    left: auto;
    margin: 0 auto;
    width: 100px;
    height: 100px;
    background: var(--ink);
  }
  .master-logo .brand-name {
    position: static;
    margin-top: 22px;
    font-size: 38px;
    line-height: 40px;
    color: var(--ink);
  }
</style>
</head>
<body>

  <section class="label label--leaf">
    <div class="brand-mark" role="img" aria-label="Brand mark"></div>
    <h2 class="brand-name">Brackenmoor<br>Organic</h2>
    <div class="product-frame"><div class="product-space"></div></div>
    <div class="certification">
      <div class="certification__council" role="img" aria-label="Tillbrook Council organic badge"></div>
      <div class="certification__eu" role="img" aria-label="European organic badge"></div>
      <p class="certification__code">GB-TRV-38<br>Non-EU Agriculture</p>
    </div>
  </section>

  <section class="label label--stone">
    <div class="brand-mark" role="img" aria-label="Brand mark"></div>
    <h2 class="brand-name">Brackenmoor<br>Organic</h2>
    <div class="product-frame"><div class="product-space"></div></div>
    <div class="certification">
      <div class="certification__council" role="img" aria-label="Tillbrook Council organic badge"></div>
      <div class="certification__eu" role="img" aria-label="European organic badge"></div>
      <p class="certification__code">GB-TRV-38<br>Non-EU Agriculture</p>
    </div>
  </section>

  <section class="label label--cream">
    <div class="brand-mark" role="img" aria-label="Brand mark"></div>
    <h2 class="brand-name">Brackenmoor<br>Organic</h2>
    <div class="product-frame"><div class="product-space"></div></div>
    <div class="certification">
      <div class="certification__council" role="img" aria-label="Tillbrook Council organic badge"></div>
      <div class="certification__eu" role="img" aria-label="European organic badge"></div>
      <p class="certification__code">GB-TRV-38<br>Non-EU Agriculture</p>
    </div>
  </section>

  <div class="master-logo">
    <div class="brand-mark" role="img" aria-label="Brand mark"></div>
    <h1 class="brand-name">Brackenmoor<br>Organic</h1>
  </div>

</body>
</html>
```